Business Card Design Project

Design is for the business card of a holistic, integral therapist. Design is required for front (colour / pattern) and back (white, with text as below).

Please prepare the design using placeholder text. I will work with the winning submission to complete the final information in the last iteration.

To give you a sense of her services a profile is below:
- I offer an integrative approach for effective relief of many issues such as anxiety, panic attacks, relationship difficulties, and health problems. In my counselling sessions I mainly use QBR {Quiet Balance Release } which taps into the body's energy system (meridians) to clear up blockages and limiting /distorted thinking and beliefs. I also work on expanding awareness as well as enhancing relationships.Clients have found the sessions life changing and report feeling lighter, clearer more empowered and connected to themselves and others.

Target Market(s)

Well educated, upper socioeconomic people seeking purpose and happiness in their lives.

Industry/Entity Type

Health

Requirements
Must have
• Must have the following text on front

First Name, Last Name
LLB, ND, Dip C
Counselling & Naturopathy
Quiet Balnce Release and Marlow Therapy

Adress 1 Line 1
Adress 1 Line 2

Adress 2 Line 1
Adress 2 Line 2

xxx.xxx@xxxxx.com

Tel: 0XXX XXX XXX

Must have the following text on reverse - which should be primarily white.

Next appointment
Date:
Time:
Nice to have
• Example colour palettes

http://www.huebinder.example/swatch/512093/velvet_lantern
http://www.huebinder.example/swatch/318420/Quiet_Orchard
http://www.huebinder.example/swatch/607215/Morning_Over_Tides

Example images that may be useful...
http://www.shopvarn.example/gp/product/images/4719205536/ref=dp_image_text_0?ie=UTF8&n=517302&s=books
http://www.shopvarn.example/gp/customer-media/product-gallery/6284019573/ref=cm_ciu_pdp_images_all
http://en.loreweb.example/wiki/File:Lotus_Grid_256bw.gif

```html
<!DOCTYPE html>
<html lang="en">
<head>
<meta charset="utf-8">
<title>Business Card – Front and Back</title>
<link rel="stylesheet" href="https://fonts.googleapis.com/css2?family=Arimo:wght@400;700&family=Tinos:wght@400&display=swap">
<style>
  :root {
    --ink: #000000;
    --paper: #ffffff;
    --card-blue-dark: #4f6d9c;
    --card-blue: #6a86b3;
    --card-blue-light: #8ea6c9;
    --strip-blue: #4b6691;
    --soft-white: #dce5f2;
    --address-grey: #c9d4e6;
    --rule-grey: #8a8a8a;
    --puzzle-light: #b9c9de;
    --puzzle-mid: #7f8fa8;
  }
  * { box-sizing: border-box; margin: 0; padding: 0; }
  html, body {
    width: 1200px; height: 1061px; overflow: hidden;
    background: var(--paper);
  }
  .canvas { position: relative; width: 1200px; height: 1061px; }

  /* Front */
  .card-front {
    position: absolute; left: 0; top: 0; width: 1200px; height: 529px;
    border: 5px solid var(--ink);
    background: linear-gradient(160deg, var(--card-blue-dark) 0%, var(--card-blue) 55%, var(--card-blue-light) 100%);
    overflow: hidden;
    font-family: "Arimo", Arial, sans-serif;
    color: var(--paper);
  }
  .puzzle-art {
    position: absolute; left: 660px; top: 10px; width: 530px; height: 380px;
    background: radial-gradient(ellipse at 55% 40%, var(--puzzle-light) 0%, var(--puzzle-mid) 45%, rgba(106,134,179,0) 75%);
  }
  .holder-name { position: absolute; left: 40px; top: 80px; font-size: 34px; font-weight: 700; }
  .credentials { position: absolute; left: 330px; top: 128px; font-size: 25px; font-weight: 700; }
  .practice { position: absolute; left: 40px; top: 174px; font-size: 28px; font-weight: 400; color: var(--soft-white); }
  .services { position: absolute; left: 40px; top: 350px; font-size: 30px; font-weight: 700; }
  .services-rule { position: absolute; left: 0; top: 400px; width: 890px; height: 7px; background: var(--ink); }
  .contact-strip {
    position: absolute; left: 0; top: 407px; width: 100%; height: 117px;
    background: var(--strip-blue);
  }
  .address { position: absolute; font-family: "Tinos", "Times New Roman", serif; font-size: 17px; line-height: 24px; color: var(--address-grey); }
  .address-one { left: 45px; top: 411px; }
  .address-two { left: 672px; top: 411px; }
  .address-icon { position: absolute; width: 30px; height: 30px; }
  .address-icon.one { left: 12px; top: 416px; }
  .address-icon.two { left: 626px; top: 425px; }
  .address-rule { position: absolute; left: 40px; top: 462px; width: 515px; height: 2px; background: var(--ink); }
  .phone { position: absolute; left: 45px; top: 488px; font-size: 20px; color: var(--soft-white); }
  .email { position: absolute; right: 30px; top: 490px; font-family: "Tinos", "Times New Roman", serif; font-size: 19px; color: var(--address-grey); }

  /* Back */
  .card-back {
    position: absolute; left: 0; top: 534px; width: 1200px; height: 527px;
    border: 8px solid var(--ink);
    background: var(--paper);
    font-family: "Arimo", Arial, sans-serif;
    color: var(--ink);
  }
  .appointment-title { position: absolute; left: 38px; top: 28px; font-size: 36px; font-weight: 700; }
  .write-line { position: absolute; left: 33px; width: 1040px; height: 2px; background: var(--rule-grey); }
  .write-line.first { top: 125px; }
  .write-line.second { top: 197px; }
  .field-label { position: absolute; left: 38px; font-size: 28px; font-weight: 700; }
  .field-label.date { top: 231px; }
  .field-label.time { top: 356px; }
</style>
</head>
<body>
<div class="canvas">
  <section class="card-front">
    <div class="puzzle-art" role="img" aria-label="Illustration of interlocking pale blue jigsaw puzzle pieces"></div>
    <div class="holder-name">First Name, Last Name</div>
    <div class="credentials">LLB, ND, Dip C</div>
    <div class="practice">Counselling &amp; Naturopathy</div>
    <div class="services">Quiet Balnce Release and Marlow Therapy</div>
    <div class="services-rule"></div>
    <div class="contact-strip"></div>

    <svg class="address-icon one" viewBox="0 0 30 30" aria-hidden="true">
      <circle cx="15" cy="15" r="13" fill="#ffffff" stroke="#000" stroke-width="2"/>
      <rect x="8" y="10" width="14" height="10" fill="none" stroke="#000" stroke-width="1.8"/>
      <path d="M8 10 L15 16 L22 10" fill="none" stroke="#000" stroke-width="1.8"/>
    </svg>
    <div class="address address-one">Adress 1 Line 1<br>Adress 1 Line 2</div>
    <div class="address-rule"></div>

    <svg class="address-icon two" viewBox="0 0 30 30" aria-hidden="true">
      <circle cx="15" cy="15" r="13" fill="#ffffff" stroke="#000" stroke-width="2"/>
      <rect x="8" y="10" width="14" height="10" fill="none" stroke="#000" stroke-width="1.8"/>
      <path d="M8 10 L15 16 L22 10" fill="none" stroke="#000" stroke-width="1.8"/>
    </svg>
    <div class="address address-two">Adress 2 Line 1<br>Adress 2 Line 2</div>

    <div class="phone">Tel: 0XXX XXX XXX</div>
    <div class="email">xxx.xxx@xxxxx.com</div>
  </section>

  <section class="card-back">
    <div class="appointment-title">Next appointment</div>
    <div class="write-line first"></div>
    <div class="write-line second"></div>
    <div class="field-label date">Date :</div>
    <div class="field-label time">Time :</div>
  </section>
</div>
</body>
</html>
```